Zielgruppe
Wir sind eine e-commerce brand auf marktora und suchen ein hochwertiges Verpackungsdesign für eine Gartenschere. Zielgruppe sind Männer 70 und Frauen 30%
Aufgabenstellung
ACHTUNG ÄNDERUNG am 23.07.2024: Typenbezeichnung: Statt 'Feder Klick' bitte 'Garten Pro' verwenden.
1 color box für die Farbvarianate grün und eine color box für die Farbvariante gelb. Größe 23.8x7.8x3cm. Je ein unterschiedlicher Barcode für jede Farbvariante muss eingefügt werden.
Wichtig: Das Produkt sollte auf der Suchergebnisseite bei marktora (Keywort Gartenschere) herausstechen.
Brand: wiesborn
Titel: Gartenschere
Typenbezeichnung: Feder Klick
Kurzbeschreibung: Klingen aus hochfestem SK5 Stahl mit Titan- Beschichtung. Stufenlose Größeneinstellung
Produktbeschreibung: Unsere hochwertige Astschere wiesborn 'Feder Klick' schneidet präzise und mühelose Schnitte für Äste und Zweige bis zu einer Stärke von 2 cm. Dank ergonomischer Griffe, scharfer Klingen aus gehärtetem Stahl inkl. Glidex- Beschichtung ist sie sowohl komfortabel als auch langlebig. Die Astschere kann für kleine oder große Hände eingestellt werden
Sicherheitshinweise: 'Sicherheitshinweise für den Gebrauch der Astschere:
- Schutzausrüstung: Das Tragen von Handschuhen und Schutzbrille wird empfohlen, um Verletzungen zu vermeiden.
- Kinder: Bewahre die Astschere außerhalb der Reichweite von Kindern auf und lasse sie nicht unbeaufsichtigt in deren Nähe.
- Verwendung: Benutze die Astschere nur für den vorgesehenen Zweck. Schneide nur Äste und Zweige, die innerhalb der empfohlenen Schneidkapazität liegen.
- Überprüfe regelmäßig alle Teile der Astschere auf Abnutzung oder Beschädigung.
Pflege & Reinigung der Schere 'Reinigungshinweise:
Entferne Pflanzensaft und Schmutz mit einem feuchten Tuch oder einer Bürste.
Verwende gegebenenfalls mildes Seifenwasser, um hartnäckigen Schmutz zu lösen.
Trockne die Gartenschere gründlich ab, um Rostbildung zu vermeiden.
Pflegehinweise:
Trage regelmäßig ein paar Tropfen Maschinen- oder Klingenöl auf die Gelenke und Klingen a..

```html
<!DOCTYPE html>
<html lang="de">
<head>
<meta charset="utf-8">
<title>wiesborn Gartenschere – Faltschachtel Gelb</title>
<link rel="stylesheet" href="https://fonts.googleapis.com/css2?family=Fira+Sans+Extra+Condensed:wght@600&family=Montserrat:wght@800;900&display=swap">
<style>
  :root {
    --page: #ffffff;
    --dieline: #e5199b;
    --brand-green: #245a2a;
    --meadow-light: #eaf9d6;
    --meadow-mid: #9fdc4a;
    --meadow-deep: #6cbf22;
    --grass: #4f9e2a;
    --tool-dark: #3b4650;
    --variant-yellow: #fbd400;
    --white: #ffffff;
  }
  html, body {
    margin: 0;
    padding: 0;
    width: 1200px;
    height: 1200px;
    overflow: hidden;
    background: var(--page);
  }
  .canvas {
    position: relative;
    width: 1200px;
    height: 1200px;
  }
  .dieline {
    position: absolute;
    inset: 0;
    width: 1200px;
    height: 1200px;
  }
  .dieline path, .dieline rect, .dieline line {
    fill: none;
    stroke: var(--dieline);
    stroke-width: 1.6;
  }
  .front-panel {
    position: absolute;
    left: 267.5px;
    top: 645px;
    width: 672px;
    height: 230px;
    overflow: hidden;
    border: 1px solid var(--dieline);
    box-sizing: border-box;
  }
  .meadow-scene {
    position: absolute;
    inset: 0;
    background:
      linear-gradient(to bottom, rgba(79,158,42,0) 62%, rgba(79,158,42,0.85) 82%, var(--grass) 100%),
      radial-gradient(ellipse at 55% 45%, var(--meadow-light) 0%, #d2f0a8 35%, var(--meadow-mid) 70%, var(--meadow-deep) 100%);
  }
  .product-photo {
    position: absolute;
    left: 392px;
    top: 24px;
    width: 268px;
    height: 180px;
    border-radius: 40% 30% 45% 35%;
    background: radial-gradient(ellipse at 55% 40%, var(--tool-dark) 0%, #56626b 45%, rgba(215,180,40,0.55) 75%, rgba(215,180,40,0) 100%);
  }
  .brand-name,
  .product-title,
  .model-pill {
    z-index: 2;
  }
  .brand-name {
    position: absolute;
    left: 0;
    width: 404px;
    top: 26px;
    text-align: center;
    font-family: "Fira Sans Extra Condensed", sans-serif;
    font-weight: 600;
    font-size: 46px;
    line-height: 1;
    color: var(--brand-green);
  }
  .product-title {
    position: absolute;
    left: 26px;
    top: 85px;
    margin: 0;
    font-family: "Montserrat", sans-serif;
    font-weight: 900;
    font-size: 39px;
    line-height: 1.1;
    letter-spacing: 0.2px;
    color: var(--brand-green);
  }
  .model-pill {
    position: absolute;
    left: 115px;
    top: 146px;
    width: 176px;
    height: 38px;
    border-radius: 19px;
    background: var(--brand-green);
    color: var(--white);
    font-family: "Montserrat", sans-serif;
    font-weight: 800;
    font-size: 19px;
    line-height: 38px;
    text-align: center;
  }
  .variant-band {
    position: absolute;
    inset: 0;
    width: 672px;
    height: 230px;
    z-index: 3;
  }
  .variant-band polygon { fill: var(--variant-yellow); }
  .variant-label {
    position: absolute;
    z-index: 4;
    left: 616px;
    top: 171px;
    transform: translate(-50%, -50%) rotate(-45deg);
    font-family: "Montserrat", sans-serif;
    font-weight: 900;
    font-size: 31px;
    line-height: 1;
    color: var(--white);
    white-space: nowrap;
  }
</style>
</head>
<body>
<div class="canvas">
  <svg class="dieline" viewBox="0 0 1920 1920" aria-hidden="true">
    <g class="dieline-center">
      <line x1="256" y1="387" x2="1675" y2="387"/>
      <line x1="412" y1="531" x2="1520" y2="531"/>
      <line x1="240" y1="889" x2="1692" y2="889"/>
      <line x1="428" y1="1032" x2="1503" y2="1032"/>
      <line x1="428" y1="1400" x2="1503" y2="1400"/>
      <line x1="420" y1="1410" x2="1512" y2="1410"/>
      <line x1="412" y1="1543" x2="1520" y2="1543"/>
    </g>
    <g id="dieline-half">
      <path d="M256 387 V512 H412 Q426 508 426 498 V387"/>
      <path d="M240 527 L226 538 H101 V634 L77 638 V774 L101 777 V882 H226 L240 889 V527 H398 L412 531"/>
      <line x1="261" y1="527" x2="261" y2="889"/>
      <line x1="404" y1="531" x2="404" y2="889"/>
      <rect x="402" y="634" width="24" height="152" rx="12"/>
      <path d="M412 889 Q412 904 400 904 H235 V1025 H412 V889"/>
      <path d="M412 1025 Q428 1025 428 1040 V1392 Q428 1410 412 1410"/>
      <path d="M428 1042 L306 1086 Q292 1092 292 1108 V1330 Q292 1350 308 1357 L428 1392"/>
      <path d="M412 1410 L330 1416 Q294 1420 300 1447 Q326 1518 400 1533 L412 1543 V1410"/>
    </g>
    <use href="#dieline-half" transform="translate(1932 0) scale(-1 1)"/>
  </svg>

  <section class="front-panel">
    <div class="meadow-scene" role="img" aria-label="Helle grüne Frühlingswiese mit unscharfem Lichthintergrund und Grashalmen am unteren Rand"></div>
    <div class="product-photo" role="img" aria-label="Produktfoto der Gartenschere mit grauen Griffen, gelben Akzenten, gelber Klinge und Handschlaufe"></div>
    <div class="brand-name">wiesborn</div>
    <h1 class="product-title">GARTENSCHERE</h1>
    <div class="model-pill">GARTEN PRO</div>
    <svg class="variant-band" viewBox="0 0 672 230" aria-hidden="true">
      <polygon points="523,230 672,80 672,167 608,230"/>
    </svg>
    <div class="variant-label">GELB</div>
  </section>
</div>
</body>
</html>
```